Radiant Stage Productions Sole Brillante Concert

I want a PORTRAIT STYLE DL size poster for a cabaret-style concert that I am promoting as part of a Community Arts Festival in Western Australia.

I WOULD LIKE A RED CHECK TABLECLOTH WITH PICNIC FOOD AND A WINE GLASS TOWARDS THE BOTTOM OF THE PAGE . WITH THE BLACK AND WHITE IMAGE OF THE MAN NOT TOO LARGE . BRIGHT RED WHITE AND GREEN COLOURS TO SHOW THE ITALIAN THEME.

The name of the concert is "Sole Brillante" which means the heart of Italy, my Italian Heart , I love italy etc.

The concert will have live music, with a 6 or 7 piece band. A variety of singers will performing lots of lovely Italian songs in different styles from Grand Opera to the songs of the 40's an 50's (Walt Brennor and Lloyd Haverty) through to modern Italian popular songs like Under the Evening Sky (Nel Vento Blu etc) it will be like a party with everyone coming on and singing their favourite Italian songs and we want the audience to sing along and have a great time.

It is important that the reader understands that they can sit and enjoy a picnic and wine package . Included in the price.
Patrons will be sitting at tables looking forward to the action on the stage.

**********************************************************************************
Text For the poster...
Radiant Stage Productions ( small font size at top of the page)

Sole Brillante! (this is the name of the concert)

Cabaret at the Harbourgate Civic Hall (the word cabaret shows that is a catered event)

"Maestro Pietro Galvani takes us on a fun filled journey from the Isle of Sicily to the canals of Venezia"

Sunday 10th November 2013
Matinee 3:00pm

Tickets
STANDARD $45 Upstairs Gallery
PREMIUM $95 Downstairs at tables with wine and gourmet picnic hamper included.

www.seatpoint-example.com.au
tel: 1300 415 908
For further info
www.loretta-bellweather.example
facebook Loretta Bellweather Concert Club
*************************************************************************************
THIS IS THE TEXT THAT IS GOING IN THE ARTS BROCHURE FOR YOUR INFORMATION : "Celebrating the best of all things Italian. Maestro Pietro Galvani takes us on a fun filled journey with his band and vocalists through various styles of Italian music and favourite classic songs. From the Isle of Sicily to the canals of Venezia, you won't be able to stop yourself singing along to these famous tunes!"

Hello Everyone,

The deadline has been extended to Wednesday.

I have updated some of the info for the brief details below.

NOTE: I have added a description of the event
decided not to have a keyboard or piano image.

I want bold colours with Italian Flag or Green, White and Red .

Clear text so the eye flows down the page to the information details.

Thanks

Target Market(s)

40 + age group...Westhaven has a very strong Italian Community we will be directly targeting the Italian Clubs in Westhaven and the Perth areas. The Musical director is well known in these clubs.

Industry/Entity Type

Club

Requirements
Must have
• The Coastline Arts Festival Tab.
Nice to have
• important that the picnic and wine element is highlighted and that there are tables. I don't want them thinking it is an outdoors event.
Bright vibrant colours
An Italian flag?

```html
<!DOCTYPE html>
<html lang="en">
<head>
<meta charset="utf-8">
<title>Sole Brillante! – Cabaret Concert</title>
<link rel="stylesheet" href="https://fonts.googleapis.com/css2?family=Lobster&family=Didact+Gothic&family=Poppins:wght@600&display=swap">
<style>
  :root{
    --red:#c8102e;
    --white:#ffffff;
    --brown:#3b2418;
    --brown-dark:#24150e;
    --green:#23852f;
    --green-dark:#166b22;
    --label-green:#7cc443;
    --flag-green:#2f8f3c;
    --flag-white:#f2f2ee;
    --flag-red:#cf2a2a;
  }
  *{margin:0;padding:0;box-sizing:border-box}
  html,body{width:1200px;height:2470px;overflow:hidden;background:var(--white)}
  .poster{position:relative;width:1200px;height:2470px;overflow:hidden;font-family:"Didact Gothic",sans-serif;color:var(--white)}
  .backdrop,.flag-photo,.maestro-photo{position:absolute;left:0;top:0}
  .flag-photo{width:1200px;height:720px}
  .maestro-photo{left:540px;top:470px;width:660px;height:960px}

  .producer-label{position:absolute;left:30px;top:112px;width:672px;height:74px;
    background:linear-gradient(90deg,var(--label-green),#a6dc6c);
    border-radius:0 10px 10px 0;padding-left:30px;
    font-size:46px;line-height:74px;color:var(--white)}

  .festival-tab{position:absolute;left:1090px;top:20px;width:86px;height:280px;background:var(--red);
    display:flex;flex-direction:column;align-items:center;padding-top:14px}
  .festival-tab .tab-name{font-size:15px;color:var(--white);display:flex;align-items:center;gap:4px}
  .festival-tab .tab-name i{width:8px;height:8px;background:var(--white);display:block}
  .festival-tab .tab-text{margin-top:16px;writing-mode:vertical-rl;font-size:17px;line-height:20px;
    text-transform:uppercase;letter-spacing:1px;color:var(--white)}

  .concert-title{position:absolute;left:60px;top:300px;font-family:"Lobster",cursive;font-size:140px;line-height:1.2;
    color:var(--red);-webkit-text-stroke:6px var(--white);paint-order:stroke fill;
    text-shadow:4px 6px 8px rgba(0,0,0,.45);white-space:nowrap}
  .tagline{position:absolute;left:66px;top:525px;font-size:56px;line-height:66px;text-transform:uppercase;white-space:nowrap}
  .heart{position:absolute;left:262px;top:680px;width:84px;height:72px}
  .intro{position:absolute;left:66px;top:790px;width:500px;font-size:42px;line-height:72px}

  .picnic-photo{position:absolute;left:62px;top:1232px;width:468px;height:580px;border:12px solid var(--white);
    transform:rotate(-3deg);box-shadow:6px 10px 18px rgba(0,0,0,.45);
    background:linear-gradient(180deg,#5a3a22 0%,#8a5a32 35%,#b04030 62%,#e05050 80%,#f3d0d0 100%)}

  .event-details{position:absolute;right:65px;top:1505px;text-align:right;font-size:44px;line-height:54px;white-space:nowrap}
  .ticket-prices{position:absolute;right:65px;top:1812px;text-align:right;font-family:"Poppins",sans-serif;font-weight:600;
    font-size:34px;line-height:54px;white-space:nowrap}

  .about-band{position:absolute;left:56px;top:2100px;width:400px;font-size:26px;line-height:36px}
  .contacts{position:absolute;right:65px;top:2265px;text-align:right;font-family:"Poppins",sans-serif;font-weight:600;
    font-size:27px;line-height:46px;white-space:nowrap}
  .contacts .social{display:inline-flex;align-items:center;gap:10px}
  .contacts .social i{width:26px;height:26px;background:var(--white);border-radius:4px;display:block}
</style>
</head>
<body>
<div class="poster">

  <svg class="flag-photo" width="1200" height="720" viewBox="0 0 1200 720" role="img" aria-label="Waving Italian flag in green, white and red">
    <defs>
      <linearGradient id="flagWave" x1="0" y1="0" x2="1" y2="0.25">
        <stop offset="0" stop-color="var(--flag-green)"/>
        <stop offset="0.3" stop-color="#4aa556"/>
        <stop offset="0.42" stop-color="var(--flag-white)"/>
        <stop offset="0.62" stop-color="#dedbd4"/>
        <stop offset="0.76" stop-color="var(--flag-red)"/>
        <stop offset="1" stop-color="#a41818"/>
      </linearGradient>
    </defs>
    <rect width="1200" height="720" fill="url(#flagWave)"/>
  </svg>

  <svg class="backdrop" width="1200" height="2470" viewBox="0 0 1200 2470" aria-hidden="true">
    <defs>
      <linearGradient id="brownPanel" x1="0" y1="0" x2="0" y2="1">
        <stop offset="0" stop-color="var(--brown)"/>
        <stop offset="1" stop-color="var(--brown-dark)"/>
      </linearGradient>
      <linearGradient id="greenPanel" x1="0" y1="0" x2="1" y2="1">
        <stop offset="0" stop-color="var(--green-dark)"/>
        <stop offset="0.5" stop-color="var(--green)"/>
        <stop offset="1" stop-color="var(--green-dark)"/>
      </linearGradient>
      <pattern id="stripes" width="18" height="18" patternUnits="userSpaceOnUse" patternTransform="rotate(45)">
        <rect width="9" height="18" fill="#ffffff" opacity="0.04"/>
      </pattern>
    </defs>
    <path d="M0,560 C280,360 640,290 1200,300 L1200,1460 L0,1460 Z" fill="url(#brownPanel)"/>
    <path d="M0,1330 C380,1430 820,1450 1200,1390 L1200,2470 L0,2470 Z" fill="url(#greenPanel)"/>
    <path d="M0,1330 C380,1430 820,1450 1200,1390 L1200,2470 L0,2470 Z" fill="url(#stripes)"/>
    <path d="M0,1300 C380,1410 820,1440 1200,1380" fill="none" stroke="var(--white)" stroke-width="34"/>
    <path d="M422,2470 C480,2330 620,2215 1200,2105" fill="none" stroke="var(--white)" stroke-width="30"/>
  </svg>

  <svg class="maestro-photo" width="660" height="960" viewBox="0 0 660 960" role="img" aria-label="Photo of the smiling maestro seated at a grand piano">
    <defs>
      <radialGradient id="maestroGlow" cx="0.6" cy="0.35" r="0.75">
        <stop offset="0" stop-color="#d69a5a"/>
        <stop offset="0.5" stop-color="#8a5530"/>
        <stop offset="1" stop-color="#3b2418" stop-opacity="0"/>
      </radialGradient>
    </defs>
    <rect width="660" height="960" fill="url(#maestroGlow)"/>
  </svg>

  <div class="producer-label">Radiant Stage Productions</div>

  <div class="festival-tab">
    <span class="tab-name"><i></i>Westhaven</span>
    <span class="tab-text">A City of Westhaven Festival Event</span>
  </div>

  <h1 class="concert-title">Sole Brillante!</h1>
  <p class="tagline">Celebrating the best<br>of all things Italian</p>

  <svg class="heart" viewBox="0 0 84 72" aria-hidden="true">
    <path d="M42,70 C20,52 2,38 2,20 C2,8 12,2 22,2 C31,2 38,8 42,15 C46,8 53,2 62,2 C72,2 82,8 82,20 C82,38 64,52 42,70 Z" fill="var(--red)"/>
  </svg>

  <p class="intro">Maestro Pietro Galvani takes us on a fun filled journey from the Isle of Sicily to the canals of Venezia</p>

  <div class="picnic-photo" role="img" aria-label="Photo of a picnic hamper, wine and food on a red check tablecloth"></div>

  <p class="event-details">Cabaret at the<br>Harbourgate Civic Hall<br>Sunday 10th November 2013<br>Matinee 3:00pm</p>

  <p class="ticket-prices">STANDARD $45 Upstairs Gallery<br>PREMIUM $95 Downstairs at tables<br>with wine and gourmet picnic hamper included.*</p>

  <p class="about-band">Come with Maestro Galvani and his band &amp; vocalists through all styles of Italian music and favourite classic songs. You definately won't be able to stop yourself singing along to these famous tunes!<br>*BOOKINGS ESSENTIAL</p>

  <p class="contacts">www.seatpoint-example.com.au<br>Tel: 1300 415 908<br>www.loretta-bellweather.example<br><span class="social"><i></i>Loretta Bellweather Concert Club</span></p>

</div>
</body>
</html>
```